BROCHURE OR FLYER PLEASE

We need a brochure design for our company TW Surfacing Contractors Limited. Our website is www.twsurfacing.example.nz. We have rented a 3m permanent booth at the dwelling vista hub in central Auckland. Their website is: www.dwellingvista.example.nz
We need to design and provide a company brochure outlining who we are, and the types of services we provide. Half of our flooring business is dedicated to basically Polished Concrete/Concrete Grinding; and the other half to resin and other floor toppings. We are based in Auckland, NZ and will be marketing to existing and new home owners essentially in Auckland. We want to contain concise information on our services and present this in a professional but sheik style. Housing in NZ is expensive so our brochure needs to be up market and user friendly. Polished concrete is more expensive that carpet so I feel it is important to list the benefits etc. I will attach our website and information regarding our products. We would like a double sided brochure. Our company colours are blue/red/black. I have attached some photo's you are welcome to use. Please refer to our website for more information www.twsurfacing.example.nz. Thank you.

Target Market(s)

Home Owners

Industry/Entity Type

Marketing

Requirements
Must have
• Company logo and contact details.

```html
<!DOCTYPE html>
<html lang="en">
<head>
<meta charset="utf-8">
<title>TW Surfacing Contractors – Brochure</title>
<link rel="stylesheet" href="https://fonts.googleapis.com/css2?family=Exo+2:ital,wght@0,300;0,400;0,600;0,700;1,300;1,400&display=swap">
<style>
  :root {
    --stage: #e9eaeb;
    --blue: #1f93d8;
    --blue-deep: #1668a8;
    --gold: #f4c41e;
    --red: #e2231a;
    --ink: #ffffff;
    --ink-soft: #dcefff;
    --floor-light: #c9cdce;
    --floor-dark: #7d8384;
  }
  * { box-sizing: border-box; margin: 0; padding: 0; }
  html, body {
    width: 1200px; height: 768px; overflow: hidden;
    background: var(--stage);
    font-family: "Exo 2", "Segoe UI", sans-serif;
    color: var(--ink);
  }
  .brochure-spread {
    position: absolute; left: 30px; top: 84px;
    width: 780px; height: 600px;
    display: flex;
    background: linear-gradient(135deg, var(--blue) 0%, var(--blue-deep) 100%);
    box-shadow: 0 8px 24px rgba(0,0,0,.15);
  }
  .panel { width: 260px; height: 100%; position: relative; padding: 28px 24px; }
  .panel + .panel { border-left: 1px solid rgba(255,255,255,.15); }

  /* panel: intro photo */
  .panel--feature { padding: 0; }
  .feature-photo {
    height: 62%;
    background: linear-gradient(160deg, #9fb8c9 0%, #f2f3f4 40%, #6c8aa3 75%, #2a5f9e 100%);
  }
  .feature-caption { padding: 20px 24px; }
  .feature-script {
    font-style: italic; font-weight: 300; font-size: 30px; line-height: 1.1;
  }
  .feature-services {
    margin-top: 12px; font-weight: 700; font-size: 13px; letter-spacing: .06em;
    text-transform: uppercase; line-height: 1.45;
  }
  .feature-services .light { font-weight: 300; }
  .social-link {
    position: absolute; left: 24px; bottom: 22px;
    display: flex; align-items: center; gap: 8px; font-size: 12px;
  }
  .social-link .dot { width: 14px; height: 14px; border-radius: 50%; background: var(--ink); }

  /* panel: about */
  .panel-title { font-size: 22px; font-weight: 600; line-height: 1.15; }
  .panel-title .gold { color: var(--gold); font-weight: 700; }
  .panel-title .sub { font-weight: 400; }
  .body-copy { margin-top: 14px; font-size: 12px; line-height: 1.55; color: var(--ink-soft); font-weight: 300; }
  .value-list { list-style: none; margin-top: 26px; display: flex; flex-direction: column; gap: 12px; }
  .value-list li { display: flex; align-items: center; gap: 10px; font-size: 14px; letter-spacing: .12em; text-transform: uppercase; }
  .value-list svg { width: 22px; height: 22px; }

  /* panel: non-slip */
  .options-heading { margin-top: 14px; font-size: 13px; font-weight: 700; }
  .options-list { margin-top: 8px; padding-left: 14px; font-size: 12px; line-height: 1.6; font-weight: 300; color: var(--ink-soft); }

  /* front cover */
  .cover {
    position: absolute; left: 850px; top: 84px;
    width: 320px; height: 600px;
    box-shadow: 0 8px 24px rgba(0,0,0,.15);
  }
  .cover-photo {
    position: absolute; inset: 0;
    background: linear-gradient(180deg, #e9e4da 0%, #b9a58a 30%, var(--floor-light) 55%, var(--floor-dark) 100%);
  }
  .cover-card {
    position: absolute; left: 34px; top: 110px; width: 252px; height: 400px;
    background: var(--blue); padding: 20px 22px;
    display: flex; flex-direction: column;
  }
  .cover-title {
    font-style: italic; font-weight: 300; font-size: 20px; line-height: 1.2; text-align: center;
    padding-bottom: 12px; border-bottom: 1px solid rgba(255,255,255,.5);
  }
  .cover-intro { margin-top: 14px; font-size: 14px; line-height: 1.35; font-weight: 300; }
  .cover-intro strong { font-weight: 700; }
  .finish-list { list-style: none; margin-top: 20px; display: flex; flex-direction: column; gap: 10px; padding-left: 24px; }
  .finish-list li { display: flex; align-items: center; gap: 10px; font-size: 14px; }
  .finish-list .num {
    width: 16px; height: 16px; border-radius: 50%; background: var(--red);
    font-size: 10px; font-weight: 700; display: grid; place-items: center;
  }
  .brand-mark {
    margin-top: auto; display: flex; align-items: center; justify-content: center; gap: 8px;
    font-size: 11px; font-weight: 600; white-space: nowrap;
  }
  .brand-mark .square { width: 14px; height: 14px; background: var(--red); flex: none; }
</style>
</head>
<body>

<section class="brochure-spread" aria-label="Brochure inside spread">
  <article class="panel panel--feature">
    <div class="feature-photo" role="img" aria-label="Photo of a modern two-storey white home with a pool and patio"></div>
    <div class="feature-caption">
      <p class="feature-script">Specialist in</p>
      <p class="feature-services">Concrete Polishing, Grinding <span class="light">and</span> Resin Floor Toppings</p>
    </div>
    <p class="social-link"><span class="dot"></span>fb.com/twsurfacing</p>
  </article>

  <article class="panel panel--about">
    <h2 class="panel-title"><span class="gold">GOLD STAR</span> Licensed Applicators <span class="sub">of Duravex Floor Toppings</span></h2>
    <p class="body-copy">Many homes and commercial spaces across New Zealand need hard-wearing, non-slip and hygienic floors that last for years.</p>
    <p class="body-copy">As licensed applicators of Duravex resin and terrazzo systems, we deliver seamless floors that are easy to clean, tough underfoot and finished to a high standard.</p>
    <p class="body-copy">Ideal in a variety of residential settings, our toppings meet health and safety needs while adding a stylish, modern look to any room in your home.</p>
    <ul class="value-list">
      <li><svg viewBox="0 0 22 22"><rect x="1" y="1" width="20" height="20" fill="none" stroke="#fff" stroke-width="1.5"/><path d="M5 11l4 4 9-10" fill="none" stroke="#fff" stroke-width="2.5"/></svg>Experience</li>
      <li><svg viewBox="0 0 22 22"><rect x="1" y="1" width="20" height="20" fill="none" stroke="#fff" stroke-width="1.5"/><path d="M5 11l4 4 9-10" fill="none" stroke="#fff" stroke-width="2.5"/></svg>Quality</li>
      <li><svg viewBox="0 0 22 22"><rect x="1" y="1" width="20" height="20" fill="none" stroke="#fff" stroke-width="1.5"/><path d="M5 11l4 4 9-10" fill="none" stroke="#fff" stroke-width="2.5"/></svg>Value</li>
    </ul>
  </article>

  <article class="panel panel--nonslip">
    <h2 class="panel-title"><span class="sub">Non-Slip Coatings</span><br>AND APPLICATIONS</h2>
    <p class="body-copy">If you have a garage, patio or pool surround that needs a safe non-slip surface, talk to us about the options.</p>
    <p class="body-copy">Our concrete systems are ideal for a number of areas around your home.</p>
    <p class="options-heading">Options may include:</p>
    <ul class="options-list">
      <li>Acid Washed Concrete – exposed finish</li>
      <li>Concrete Grinding and Sealing</li>
      <li>Non-slip Resin Coatings</li>
      <li>Flake Finish – decorative and durable</li>
      <li>Duravex Stoneguard – non slip flooring</li>
    </ul>
  </article>
</section>

<section class="cover" aria-label="Brochure front cover">
  <div class="cover-photo" role="img" aria-label="Photo of a polished concrete floor in a bright living room"></div>
  <div class="cover-card">
    <h1 class="cover-title">A variety of finishes for your concrete floors</h1>
    <p class="cover-intro">Looking to achieve a particular look with your concrete floors? <strong>We have a range of sealing products</strong> which provide different finishes for your floor, including...</p>
    <ol class="finish-list">
      <li><span class="num">1</span>Glass</li>
      <li><span class="num">2</span>Semi-glass</li>
      <li><span class="num">3</span>Matte</li>
    </ol>
    <p class="brand-mark"><span class="square"></span>TW Surfacing Contractors Limited</p>
  </div>
</section>

</body>
</html>
```